Ecommerce Website For Printing Company

Zoravquill.com are a print, design and signage company who sell flyers, business cards, posters, brochures and more to customers in the UK.

Our website is outdated and requires a new design using current web styling and mobile functionality.

We require the following pages to be designed;
- Home Page
- Price Page
- Portfolio Page
- Blog
- Content Page

Our competitors in the printing industry are www.brenticade.com, www.hallowmarsh.co.uk, quorelvane.co.uk, www.tambridok.co.uk

We require the website to give a professional image as well as be easy for customers to navigate, understand and find prices.

Target Market(s)

Businesses

Industry/Entity Type

Printing

Number of Pages Required

4 page

Font styles to use
Sans Serif

Colors
33a6d7

Requirements
Must have
• Popular products, latest news/blog, sales from portfolio, newsletter sign up, footer

```html
<!DOCTYPE html>
<html lang="en">
<head>
<meta charset="utf-8">
<title>Zoravquill.com – Print, Design &amp; Signage</title>
<link href="https://fonts.googleapis.com/css2?family=Open+Sans:wght@400;600;700;800&display=swap" rel="stylesheet">
<style>
:root{
  --brand:#33a6d7;
  --navy:#0c3470;
  --navy-dark:#082a5c;
  --ink:#2b2b2b;
  --muted:#7a7a7a;
  --line:#e3e3e3;
  --panel:#f2f2f2;
  --lime:#b6d432;
  --red:#d0162c;
  --white:#fff;
}
*{box-sizing:border-box;margin:0;padding:0}
html,body{width:1200px;height:2832px;overflow:hidden}
body{font-family:"Open Sans",Arial,sans-serif;color:var(--ink);background:var(--white);font-size:14px}
.wrap{width:896px;margin:0 auto;position:relative}
a{color:inherit;text-decoration:none}

/* utility bar */
.utility{height:44px;border-bottom:1px solid var(--line);font-size:11px;font-weight:600;color:#555}
.utility .wrap{display:flex;align-items:center;height:44px;gap:22px}
.utility span{display:flex;align-items:center;gap:6px}
.utility i{display:inline-block;width:10px;height:10px;border-radius:50%;background:#999}

/* header */
.header{height:108px}
.header .wrap{display:flex;align-items:center;height:108px}
.logo{display:flex;align-items:center;gap:10px;font-size:34px;font-weight:800;color:var(--navy);letter-spacing:-.5px}
.logo .mark{width:22px;height:22px;background:var(--brand)}
.phone{margin-left:auto;display:flex;align-items:center;gap:8px;font-size:22px;font-weight:700;color:var(--navy)}
.phone svg{width:22px;height:22px}
.search{margin-left:36px;display:flex;height:34px;border:1px solid #ccc}
.search input{width:156px;border:0;padding:0 10px;font:12px "Open Sans",sans-serif}
.search button{width:34px;border:0;background:var(--navy)}
.cart{margin-left:12px;height:34px;padding:0 16px;background:var(--navy);color:#fff;font-size:12px;font-weight:700;display:flex;align-items:center}

/* nav */
.nav{height:40px;background:#f7f7f7;border-top:1px solid var(--line);border-bottom:3px solid var(--navy)}
.nav ul{list-style:none;display:flex;height:37px}
.nav li{padding:0 16px;display:flex;align-items:center;font-size:12px;font-weight:700;color:var(--navy);white-space:nowrap}
.nav li.active{background:var(--navy);color:#fff}

/* hero */
.hero{height:320px;background:linear-gradient(90deg,#3a1f6e,#6a1e5a 55%,#7a2040);position:relative}
.hero .wrap{height:320px}
.hero-art{position:absolute;left:0;top:20px;width:440px;height:280px;background:linear-gradient(135deg,#4a8fd0,#e8e4da 60%,#c75a3a);border-radius:4px}
.hero-copy{position:absolute;left:520px;top:36px;color:#fff}
.hero-copy h1{font-size:60px;font-weight:800;letter-spacing:1px;line-height:1}
.hero-copy p.lead{font-size:20px;line-height:1.35;margin-top:12px}
.save{display:flex;align-items:center;gap:14px;margin-top:18px}
.save .pct{font-size:64px;font-weight:800;color:#ffb21a;line-height:1}
.save .pct small{display:block;font-size:13px;color:#fff;font-weight:600}
.btn-red{background:var(--red);color:#fff;font-size:12px;font-weight:700;padding:8px 14px;display:inline-block}
.hero-copy .tag{font-size:22px;margin-top:14px}
.arrow{position:absolute;top:140px;width:24px;height:40px;background:rgba(0,0,0,.45);display:flex;align-items:center;justify-content:center}
.arrow.l{left:0}.arrow.r{right:0}

/* quote + tiles */
.shop{display:flex;gap:16px;margin-top:20px}
.quote{width:320px;background:var(--panel);border:1px solid var(--line)}
.quote-head{background:var(--navy);color:#fff;padding:14px 16px;display:flex;gap:12px;align-items:center}
.quote-head .ico{width:44px;height:44px;border:2px solid #fff;border-radius:4px}
.quote-head b{font-size:20px;line-height:1.05;display:block}
.quote-head small{font-size:10px;display:block;margin-top:4px}
.qrow{display:flex;align-items:center;gap:10px;padding:0 16px;height:40px;font-size:12px;color:#555;border-bottom:1px solid var(--line)}
.qrow .sel{margin-left:auto;width:150px;height:26px;background:#fff;border:1px solid #ccc}
.qprice{text-align:center;padding:16px;font-size:22px;font-weight:700;color:var(--red)}
.qopt{padding:0 16px;height:30px;display:flex;align-items:center;gap:8px;font-size:11px;font-weight:700;color:#444}
.qopt:before{content:"";width:10px;height:10px;background:var(--navy)}
.qtotal{margin:14px 0 0;background:var(--navy);color:#fff;display:flex;justify-content:space-between;padding:14px 16px;font-size:18px;font-weight:800}
.qcheck{text-align:center;padding:14px 0 18px}
.qcheck .btn-red{padding:10px 34px}
.tiles{flex:1;display:grid;grid-template-columns:1fr 1fr;gap:12px;align-content:start}
.tile{height:240px;background:#e9e9ec;position:relative;border:1px solid var(--line)}
.tile h3{position:absolute;top:18px;left:0;right:0;text-align:center;font-size:13px;font-weight:700;color:var(--navy);letter-spacing:.5px}
.tile .art{position:absolute;left:70px;right:70px;top:70px;bottom:30px;border-radius:3px}
.callbar{grid-column:1/3;height:70px;margin-top:36px;background:var(--lime);display:flex;align-items:center;gap:16px;padding:0 26px;color:var(--navy);overflow:hidden}
.callbar svg{width:34px;height:34px;flex:none}
.callbar p{font-size:15px;font-weight:700;line-height:1.25;white-space:nowrap}
.callbar p b{display:block;font-size:20px;font-weight:800}

/* section heading */
.sec-title{text-align:center;font-size:24px;font-weight:800;color:var(--navy);letter-spacing:.5px}
.sec-title:after{content:"";display:block;width:40px;height:3px;background:var(--brand);margin:10px auto 0}

/* popular products */
.popular{margin-top:44px}
.products{display:grid;grid-template-columns:repeat(4,1fr);gap:20px;margin-top:28px}
.product{text-align:center}
.product .art{height:196px;border:1px solid var(--line);background:#f4f4f4;position:relative}
.product .art div{position:absolute;inset:14px 40px}
.product h4{font-size:12px;font-weight:700;margin-top:10px}
.product .price{font-size:14px;font-weight:700;color:var(--red);margin-top:4px}

/* portfolio */
.portfolio{margin-top:36px;background:#f1f1f1;height:320px;padding-top:26px}
.folio{display:grid;grid-template-columns:repeat(5,1fr);gap:16px;margin-top:22px}
.card{background:#fff;border:1px solid var(--line);height:210px;position:relative}
.card .art{height:100px;margin:10px;position:relative}
.badge{position:absolute;left:-4px;top:-4px;width:38px;height:38px;border-radius:50%;background:var(--red);color:#fff;font-size:10px;font-weight:800;display:flex;align-items:center;justify-content:center}
.card h5{font-size:11px;font-weight:700;padding:0 10px}
.card p{font-size:9px;color:var(--muted);padding:3px 10px 0;line-height:1.3}
.card .foot{position:absolute;left:10px;right:10px;bottom:10px;display:flex;justify-content:space-between;align-items:center}
.card .foot a{background:var(--navy);color:#fff;font-size:9px;font-weight:700;padding:4px 7px}
.card .foot span{font-size:10px;font-weight:700;color:var(--red)}

/* blog */
.blog{margin-top:22px}
.posts{display:grid;grid-template-columns:repeat(4,1fr);gap:20px;margin-top:26px}
.post .art{height:120px}
.post h4{font-size:12px;font-weight:700;margin-top:12px}
.post p{font-size:10px;color:var(--muted);line-height:1.5;margin-top:6px}
.post a{display:block;font-size:10px;font-weight:700;color:var(--navy);margin-top:8px}

/* features */
.features{margin-top:32px;border-top:1px solid var(--line);border-bottom:1px solid var(--line);height:80px}
.features .wrap{display:flex;height:80px;align-items:center}
.feat{flex:1;display:flex;align-items:center;gap:12px}
.feat svg{width:34px;height:34px}
.feat b{display:block;font-size:12px;font-weight:700;color:var(--navy)}
.feat small{font-size:10px;color:var(--muted)}
.cards{display:flex;gap:6px;margin-top:6px}
.cards i{width:34px;height:20px;border-radius:2px;background:#c9ced6}

/* footer */
.footer{margin-top:20px;background:var(--navy);height:480px;color:#cdd6e6}
.footer .cols{display:grid;grid-template-columns:1.3fr 1fr 1fr 1fr;gap:30px;padding-top:40px}
.footer h6{font-size:13px;font-weight:700;color:#fff;margin-bottom:16px}
.footer p{font-size:11px;line-height:1.6}
.footer ul{list-style:none;font-size:11px;line-height:2}
.sub{display:flex;flex-direction:column;gap:10px;margin-top:14px}
.sub input{height:34px;border:0;padding:0 10px;font:11px "Open Sans",sans-serif;width:240px}
.sub .btn-red{width:100px;text-align:center}
.legal{position:absolute;left:0;top:300px;font-size:10px;line-height:1.7}
.seals{position:absolute;right:0;top:296px;display:flex;gap:10px}
.seals i{width:44px;height:44px;border-radius:50%;background:#c9a93a}
</style>
</head>
<body>

<div class="utility"><div class="wrap">
  <span><i></i>MY ACCOUNT</span><span><i></i>ORDER STATUS</span><span><i></i>BLOG</span><span><i></i>ORBITLY+</span><span><i></i>CONTACT US</span>
</div></div>

<header class="header"><div class="wrap">
  <div class="logo"><span class="mark"></span>Zoravquill.com</div>
  <div class="phone"><svg viewBox="0 0 24 24"><path fill="#0c3470" d="M6.6 10.8a15 15 0 006.6 6.6l2.2-2.2c.3-.3.7-.4 1-.2 1.1.4 2.3.6 3.6.6.6 0 1 .4 1 1V20c0 .6-.4 1-1 1A17 17 0 013 4c0-.6.4-1 1-1h3.5c.6 0 1 .4 1 1 0 1.3.2 2.5.6 3.6.1.3 0 .7-.2 1z"/></svg>01632 960 418</div>
  <div class="search"><input value="Search"><button aria-label="Search"><svg viewBox="0 0 24 24" width="16" height="16"><circle cx="10" cy="10" r="6" stroke="#fff" stroke-width="2.4" fill="none"/><path d="M15 15l5 5" stroke="#fff" stroke-width="2.4"/></svg></button></div>
  <div class="cart">MY CART</div>
</div></header>

<nav class="nav"><div class="wrap"><ul>
  <li class="active">ABOUT</li><li>PRINTING</li><li>GRAPHIC DESIGN</li><li>WEBSITE DESIGN</li><li>ARTWORK GUIDE</li><li>SAMPLE PACK</li><li>UPLOAD</li><li>TESTIMONIALS</li>
</ul></div></nav>

<section class="hero">
  <div class="arrow l"><svg width="10" height="16"><path d="M8 2L2 8l6 6" stroke="#fff" stroke-width="2" fill="none"/></svg></div>
  <div class="arrow r"><svg width="10" height="16"><path d="M2 2l6 6-6 6" stroke="#fff" stroke-width="2" fill="none"/></svg></div>
  <div class="wrap">
    <div class="hero-art" role="img" aria-label="Fanned brochure samples with a playful dog mascot"></div>
    <div class="hero-copy">
      <h1>BROCHURES</h1>
      <p class="lead">Full Colour, High Quality Brochures<br>Printing, Prices, Design and More!</p>
      <div class="save"><div class="pct"><small>Save up to</small>50%</div><span class="btn-red">SHOP NOW</span></div>
      <p class="tag">Simply put, a smarter way to print!</p>
    </div>
  </div>
</section>

<div class="wrap">
  <div class="shop">
    <aside class="quote">
      <div class="quote-head"><span class="ico"></span><div><b>QUICK<br>QUOTE</b><small>Get an instant price online</small></div></div>
      <div class="qrow">Product<span class="sel"></span></div>
      <div class="qrow">Size<span class="sel"></span></div>
      <div class="qrow">Paper<span class="sel"></span></div>
      <div class="qrow">Quantity<span class="sel"></span></div>
      <div class="qprice">From £345.00</div>
      <div class="qopt">DESIGN PRODUCT</div>
      <div class="qopt">PRINT PRODUCT</div>
      <div class="qopt">PREMIUM PAPER</div>
      <div class="qopt">TURNAROUND</div>
      <div class="qtotal"><span>TOTAL</span><span>£345.00</span></div>
      <div class="qcheck"><span class="btn-red">CHECKOUT</span></div>
    </aside>
    <div class="tiles">
      <div class="tile"><h3>BUSINESS CARDS</h3><div class="art" role="img" aria-label="Stack of printed business cards" style="background:linear-gradient(135deg,#f2f2f2,#e8a23a)"></div></div>
      <div class="tile"><h3>POSTCARDS</h3><div class="art" role="img" aria-label="Printed postcards" style="background:linear-gradient(135deg,#f7f7f7,#d44a3a)"></div></div>
      <div class="tile"><h3>BROCHURES</h3><div class="art" role="img" aria-label="Open printed brochure" style="background:linear-gradient(135deg,#2a6fb0,#e6e6e6)"></div></div>
      <div class="tile"><h3>GRAND FORMAT PRINTING</h3><div class="art" role="img" aria-label="Large format print samples" style="background:linear-gradient(135deg,#e9e9e9,#c43a6a)"></div></div>
      <div class="callbar">
        <svg viewBox="0 0 24 24"><path fill="#0c3470" d="M6.6 10.8a15 15 0 006.6 6.6l2.2-2.2c.3-.3.7-.4 1-.2 1.1.4 2.3.6 3.6.6.6 0 1 .4 1 1V20c0 .6-.4 1-1 1A17 17 0 013 4c0-.6.4-1 1-1h3.5c.6 0 1 .4 1 1 0 1.3.2 2.5.6 3.6.1.3 0 .7-.2 1z"/></svg>
        <p>GOT QUESTIONS ABOUT OUR PRICING?<b>CALL US TOLL FREE AT (01632 960 000)</b></p>
      </div>
    </div>
  </div>

  <section class="popular">
    <h2 class="sec-title">POPULAR PRODUCTS</h2>
    <div class="products">
      <div class="product"><div class="art"><div role="img" aria-label="Roll-up banner stand" style="background:linear-gradient(#2c7bc0,#f0a630)"></div></div><h4>ROLLUP BANNER</h4><div class="price">£18.00</div></div>
      <div class="product"><div class="art"><div role="img" aria-label="Business card designs" style="background:linear-gradient(135deg,#fff,#2a62a8)"></div></div><h4>BUSINESS CARDS</h4><div class="price">£18.00</div></div>
      <div class="product"><div class="art"><div role="img" aria-label="A4 flyers and leaflets" style="background:linear-gradient(135deg,#f2d24a,#2a86c8)"></div></div><h4>A4 FLYERS &amp; LEAFLETS</h4><div class="price">£18.00</div></div>
      <div class="product"><div class="art"><div role="img" aria-label="Poster design" style="background:linear-gradient(#c86a2a,#f2e2c0)"></div></div><h4>POSTER DESIGN</h4><div class="price">£18.00</div></div>
    </div>
  </section>
</div>

<section class="portfolio">
  <div class="wrap">
    <h2 class="sec-title">SALES FROM PORTFOLIO</h2>
    <div class="folio">
      <div class="card"><div class="art" role="img" aria-label="Printed table cover" style="background:linear-gradient(#222,#555)"><span class="badge">-40%</span></div><h5>Table Covers</h5><p>Full colour fitted covers for events and shows.</p><div class="foot"><a>SEE DETAILS</a><span>From £175</span></div></div>
      <div class="card"><div class="art" role="img" aria-label="Booklets and catalogues" style="background:linear-gradient(135deg,#c23a3a,#2a4a8a)"><span class="badge">-40%</span></div><h5>Booklets / Catalogs</h5><p>Stitched booklets in many sizes and papers.</p><div class="foot"><a>SEE DETAILS</a><span>From £92</span></div></div>
      <div class="card"><div class="art" role="img" aria-label="Holiday greeting cards" style="background:linear-gradient(135deg,#1e6a3a,#d8b04a)"><span class="badge">-40%</span></div><h5>Holiday Cards</h5><p>Seasonal cards printed on premium stock.</p><div class="foot"><a>SEE DETAILS</a><span>From £88</span></div></div>
      <div class="card"><div class="art" role="img" aria-label="Printed flyers" style="background:linear-gradient(135deg,#f0a020,#2a7ac0)"><span class="badge">-40%</span></div><h5>Flyers</h5><p>Single or double sided glossy flyers.</p><div class="foot"><a>SEE DETAILS</a><span>From £60</span></div></div>
      <div class="card"><div class="art" role="img" aria-label="Card mailers" style="background:linear-gradient(135deg,#e6e6e6,#3a6ab0)"><span class="badge">-40%</span></div><h5>Card Sheets</h5><p>Fold cards and mailers for any campaign.</p><div class="foot"><a>SEE DETAILS</a><span>From £154</span></div></div>
    </div>
  </div>
</section>

<div class="wrap">
  <section class="blog">
    <h2 class="sec-title">LATEST BLOG / NEWS</h2>
    <div class="posts">
      <div class="post"><div class="art" role="img" aria-label="Team photo at a print event" style="background:linear-gradient(135deg,#5a4a3a,#c8a888)"></div><h4>Standing Out</h4><p>We have put together a few simple tips on how printed materials help your brand stand out from the crowd this season.</p><a>Continue Reading</a></div>
      <div class="post"><div class="art" role="img" aria-label="Football club pitch-side signage" style="background:linear-gradient(135deg,#2a5a9a,#8ab04a)"></div><h4>American Football Sign</h4><p>We have put together a short case study on the large signs we printed and fitted for a local sports club ground.</p><a>Continue Reading</a></div>
      <div class="post"><div class="art" role="img" aria-label="Printed wallpaper in a room" style="background:linear-gradient(135deg,#3a3a3a,#b8b0a0)"></div><h4>Digital Wallpaper Now Offered</h4><p>We have put together a guide to our new digital wallpaper range, printed to any size for homes and offices.</p><a>Continue Reading</a></div>
      <div class="post"><div class="art" role="img" aria-label="Oversized charity cheque presentation" style="background:linear-gradient(135deg,#6a8ab0,#e0d0b0)"></div><h4>Charity Cheque Printing</h4><p>We have put together examples of giant charity cheques printed for local fundraisers and community events.</p><a>Continue Reading</a></div>
    </div>
  </section>
</div>

<section class="features"><div class="wrap">
  <div class="feat"><svg viewBox="0 0 34 34"><rect x="2" y="10" width="18" height="14" fill="none" stroke="#0c3470" stroke-width="2"/><path d="M20 14h7l5 5v5H20z" fill="none" stroke="#0c3470" stroke-width="2"/><circle cx="9" cy="26" r="3" fill="#0c3470"/><circle cx="26" cy="26" r="3" fill="#0c3470"/></svg><div><b>FREE DELIVERY</b><small>On all orders over £50</small></div></div>
  <div class="feat"><svg viewBox="0 0 34 34"><path d="M4 6h26v18H14l-6 6v-6H4z" fill="none" stroke="#0c3470" stroke-width="2"/></svg><div><b>LIVE CHAT</b><small>Talk to our team now</small></div></div>
  <div class="feat"><div><b>PAYMENT METHOD</b><div class="cards"><i></i><i></i><i></i><i></i></div></div></div>
</div></section>

<footer class="footer"><div class="wrap">
  <div class="cols">
    <div><h6>SUBSCRIBE OUR NEWSLETTER</h6><p>Enter your email below to receive our latest offers, print tips and news.</p><div class="sub"><input value="Enter your email"><span class="btn-red">SUBSCRIBE</span></div></div>
    <div><h6>PRODUCT &amp; SERVICES</h6><ul><li>Products &amp; Services</li><li>Offset Printing</li><li>Large Format Printing</li><li>Promo Products</li><li>Design Services</li></ul></div>
    <div><h6>GET STARTED</h6><ul><li>Sign up</li><li>How to order</li><li>Testimonials</li><li>Sample Pack</li></ul></div>
    <div><h6>PRODUCT &amp; SERVICES</h6><ul><li>About</li><li>Testimonials</li><li>FAQs</li><li>File Preparation</li><li>Templates</li><li>Careers</li><li>Contact Us</li></ul></div>
  </div>
  <p class="legal">Copyright 2016 Zoravquill.com. All Rights Reserved.<br>Terms &amp; Conditions · Privacy Policy · Cookie Policy</p>
  <div class="seals"><i></i><i></i><i></i></div>
</div></footer>

</body>
</html>
```